Professional Business Cards for Recruiting Company

We'd like professional 2-sided business cards that reflect a color scheme that matches our website, www.quillmerbay.com, and / or logo that is attached.

Slogan used is "We Find Talent", but needs to be editable because we change it up to "We Know Developers", "We Speak Geek", etc.

Must includes logo, slogan, first and last name, address, email, mobile number and website address.

Files attached for ideas.

Thanks!

Contact Information for Business Card

Logo, Company name, First name, Last name, addresss, email, phone, website address.

Font styles to use
Sans Serif

Colors
0054AA
0677BA
7BADD7
CADEEF
E8F1F8

Requirements
Nice to have
• I do like the following designs. 22962062 and 22962651. Couple ideas anyway.

```html
<!DOCTYPE html>
<html lang="en">
<head>
<meta charset="utf-8">
<title>Quillmerbay Business Card</title>
<link href="https://fonts.googleapis.com/css2?family=Poppins:wght@300;400;600;700&display=swap" rel="stylesheet">
<style>
  :root {
    --page: #cbcbcb;
    --slate: #5a7074;
    --navy: #152433;
    --mist: #8fa3a8;
    --steel: #74898f;
  }
  * { margin: 0; padding: 0; box-sizing: border-box; }
  html, body { width: 1200px; height: 846px; overflow: hidden; }
  body {
    background: var(--page);
    font-family: "Poppins", sans-serif;
    position: relative;
  }
  .card {
    position: absolute;
    left: 346px;
    width: 509px;
    height: 291px;
    overflow: hidden;
  }
  .card-front { top: 113px; background: var(--slate); color: var(--navy); }
  .card-back { top: 444px; background: var(--navy); }

  .front-accent { position: absolute; left: 0; top: 168px; }

  .brand { position: absolute; left: 92px; top: 46px; height: 60px; display: flex; align-items: center; gap: 9px; }
  .brand-square { width: 54px; height: 54px; border: 2px solid var(--navy); }
  .brand-text { display: flex; flex-direction: column; }
  .brand-name { font-size: 25px; font-weight: 300; letter-spacing: 0.3px; line-height: 1.05; border-bottom: 1px solid var(--navy); padding-bottom: 1px; }
  .brand-tagline { font-size: 6px; font-weight: 600; letter-spacing: 0.75px; text-transform: uppercase; margin-top: 3px; white-space: nowrap; }

  .person-name { position: absolute; left: 160px; top: 121px; font-size: 20px; font-weight: 600; line-height: 1.3; }

  .contact-list { position: absolute; left: 134px; top: 160px; list-style: none; }
  .contact-item { display: flex; align-items: center; height: 24.3px; font-size: 14px; font-weight: 400; white-space: nowrap; }
  .contact-icon { width: 20px; height: 20px; margin-right: 7px; display: flex; justify-content: center; align-items: center; }
  .contact-icon svg { width: 18px; height: 18px; fill: var(--navy); }

  .back-brand { position: absolute; left: 0; right: 0; top: 103px; display: flex; justify-content: center; align-items: center; gap: 12px; }
  .back-square { width: 36px; height: 36px; border: 2px solid var(--steel); }
  .back-name { font-size: 31px; font-weight: 600; color: var(--steel); }

  .slogan { position: absolute; left: 0; right: 0; top: 216px; text-align: center; font-size: 24px; font-weight: 700; color: var(--mist); }
  .slogan-accent { color: var(--steel); }
</style>
</head>
<body>
  <section class="card card-front">
    <svg class="front-accent" width="43" height="84" viewBox="0 0 43 84"><polygon points="0,0 42,42 0,84" fill="var(--navy)"/></svg>

    <div class="brand">
      <span class="brand-square"></span>
      <div class="brand-text">
        <span class="brand-name">QUILLMERBAY</span>
        <span class="brand-tagline">Careful staffing for growing teams</span>
      </div>
    </div>

    <h1 class="person-name">Dana Holvik</h1>

    <ul class="contact-list">
      <li class="contact-item">
        <span class="contact-icon"><svg viewBox="0 0 24 24"><path d="M7 2c1 0 1.5.6 1.8 1.5l1 3.3c.2.8-.1 1.4-.8 1.8l-1.4.8c.4 2.8 1.8 5.6 3.9 7.5l1.3-.9c.7-.5 1.4-.4 2 .2l2.3 2.3c.6.6.6 1.4 0 2l-1.3 1.4C14 24 9.5 20.5 7 16 4.8 12 4.4 7 5 4.2 5.3 2.8 6 2 7 2z"/></svg></span>
        555-014-2280 ext. 101
      </li>
      <li class="contact-item">
        <span class="contact-icon"><svg viewBox="0 0 24 24"><path d="M2 5h20v14H2z M3.5 6.5l8.5 7 8.5-7" fill="none" stroke="var(--navy)" stroke-width="1.6"/><path d="M2 5h20l-10 8z"/></svg></span>
        dana.holvik@quillmerbay.com
      </li>
      <li class="contact-item">
        <span class="contact-icon"><svg viewBox="0 0 24 24" fill="none" stroke="var(--navy)" stroke-width="1.3" style="fill:none"><circle cx="12" cy="12" r="10"/><ellipse cx="12" cy="12" rx="4.5" ry="10"/><path d="M2 12h20M4 6.5h16M4 17.5h16M12 2v20"/></svg></span>
        www.quillmerbay.com
      </li>
      <li class="contact-item">
        <span class="contact-icon"><svg viewBox="0 0 24 24"><path d="M12 1a7.5 7.5 0 0 0-7.5 7.5C4.5 14 12 23 12 23s7.5-9 7.5-14.5A7.5 7.5 0 0 0 12 1zm0 10.3a2.8 2.8 0 1 1 0-5.6 2.8 2.8 0 0 1 0 5.6z"/></svg></span>
        Ridgeford, North Dakota
      </li>
    </ul>
  </section>

  <section class="card card-back">
    <div class="back-brand">
      <span class="back-square"></span>
      <span class="back-name">Quillmerbay</span>
    </div>
    <p class="slogan">We Find <span class="slogan-accent">Talent</span></p>
  </section>
</body>
</html>
```